Bolt Ridge Hoist Service Business Cards

I need a business card for "Bolt Ridge Hoist and Tackle"

Boltridge2023@hoistmail.example

Hoist Works LLC, Bolt Ridge Hoist and Tackle LLC

555.204.7186 | www.BOLTRIDGEHOISTS.example

Central Indiana & Northeast Ohio

(IN) 23810 Meadow Lane Noblesville, IN 46099

(OH) 4150 Dunmore Street Akron, Ohio 44397

Contact Information for Business Card

Colors
0094D4
00A9DD
6FCCEA
C7EBF8
E9F6FB
59FF00
82FF00
B8FF75
E3FFCB
F4FFEA
EE7325
F08F49
F5BC92
FAE3D3
FDF4ED
EB3D1F
EC4F4E
F09395
F8D3D4
FCEDEE
E54698
E96AAD
F1A4CE
F9D9EA
FCEFF6
A7469A
B969AE
D3A5CF
EDDBEB
F8F0F9

```html
<!DOCTYPE html>
<html lang="en">
<head>
<meta charset="utf-8">
<title>Bolt Ridge Hoist and Tackle – Business Cards</title>
<link href="https://fonts.googleapis.com/css2?family=Open+Sans:wght@400;600;700&display=swap" rel="stylesheet">
<style>
  :root {
    --stage: #3b3b3f;
    --card: #28282c;
    --white: #ffffff;
    --red: #eb3d1f;
    --green: #59c93a;
    --illus-grey: #5c5c60;
  }
  * { box-sizing: border-box; margin: 0; padding: 0; }
  html, body { width: 1200px; height: 780px; overflow: hidden; }
  body {
    background: var(--stage);
    font-family: "Open Sans", sans-serif;
    display: flex;
    align-items: center;
    justify-content: center;
    gap: 24px;
  }
  .card {
    position: relative;
    width: 564px;
    height: 322px;
    background: var(--card);
    border-bottom: 3px solid var(--red);
    border-left: 3px solid var(--red);
    overflow: hidden;
  }
  /* front */
  .card-front {
    display: flex;
    align-items: center;
    justify-content: center;
  }
  .brand {
    display: flex;
    align-items: center;
    gap: 12px;
  }
  .brand-mark {
    width: 18px;
    height: 18px;
    background: var(--green);
  }
  .brand-name {
    color: var(--white);
    font-weight: 700;
    font-size: 28px;
    letter-spacing: 0.5px;
  }
  /* back */
  .corner-tab {
    position: absolute;
    top: 22px;
    right: 0;
    width: 22px;
    height: 52px;
    background: var(--red);
  }
  .company-lines {
    position: absolute;
    top: 22px;
    right: 34px;
    text-align: right;
    font-weight: 600;
    font-size: 20px;
    line-height: 26px;
  }
  .company-primary { color: var(--red); }
  .company-secondary { color: var(--green); }
  .service-area {
    position: absolute;
    top: 100px;
    right: 34px;
    text-align: right;
    color: var(--white);
    font-size: 12px;
    line-height: 19px;
    white-space: nowrap;
  }
  .contact-list {
    position: absolute;
    top: 190px;
    right: 34px;
    list-style: none;
    color: var(--white);
    font-size: 13px;
    line-height: 22px;
    white-space: nowrap;
  }
  .contact-list li {
    display: flex;
    justify-content: flex-end;
    align-items: center;
    gap: 8px;
  }
  .contact-icon { width: 12px; height: 12px; }
  .fleet-illustration {
    position: absolute;
    left: 22px;
    bottom: 10px;
    width: 190px;
    height: 200px;
    background: linear-gradient(135deg, var(--red) 0%, var(--illus-grey) 45%, var(--green) 100%);
    opacity: 0.85;
  }
</style>
</head>
<body>

  <section class="card card-front" aria-label="Card front">
    <div class="brand">
      <span class="brand-mark"></span>
      <span class="brand-name">Bolt Ridge Hoist and Tackle</span>
    </div>
  </section>

  <section class="card card-back" aria-label="Card back">
    <span class="corner-tab"></span>
    <div class="company-lines">
      <p class="company-primary">Hoist Works LLC</p>
      <p class="company-secondary">Bolt Ridge Hoist &amp; Tackle LLC</p>
    </div>
    <div class="service-area">
      <p>Central Indiana &amp; Northeast Ohio</p>
      <p>(IN) 23810 Meadow Lane Noblesville, IN 46099</p>
      <p>(OH) 4150 Dunmore Street Akron, Ohio 44397</p>
    </div>
    <ul class="contact-list">
      <li>555.204.7186
        <svg class="contact-icon" viewBox="0 0 24 24"><path fill="#eb3d1f" d="M6.6 10.8a15 15 0 0 0 6.6 6.6l2.2-2.2a1 1 0 0 1 1-.25 11.4 11.4 0 0 0 3.6.57 1 1 0 0 1 1 1V20a1 1 0 0 1-1 1A17 17 0 0 1 3 4a1 1 0 0 1 1-1h3.5a1 1 0 0 1 1 1c0 1.25.2 2.45.57 3.57a1 1 0 0 1-.25 1z"/></svg>
      </li>
      <li>www.boltridgehoists.example
        <svg class="contact-icon" viewBox="0 0 24 24"><circle cx="12" cy="12" r="10" fill="none" stroke="#eb3d1f" stroke-width="2.4"/><path d="M2 12h20M12 2c3 3 3 17 0 20M12 2c-3 3-3 17 0 20" fill="none" stroke="#eb3d1f" stroke-width="2"/></svg>
      </li>
      <li>Boltridge2023@hoistmail.example
        <svg class="contact-icon" viewBox="0 0 24 24"><rect x="2" y="5" width="20" height="14" fill="#eb3d1f"/><path d="M2 5l10 8 10-8" fill="none" stroke="#28282c" stroke-width="2"/></svg>
      </li>
    </ul>
    <div class="fleet-illustration" role="img" aria-label="Illustration of a red truck-mounted crane and a green mobile crane in front of a grey city skyline"></div>
  </section>

</body>
</html>
```